Maison Corvel

I am actually making my own traditional french food.
Everything is homemade with passion.
I make differente terrines, jams, macaroons, rillettes and much more
I do as well cocktail party and catering
Updates

Hello everyone,

On the business card I would like to see appear if it's possible these following informations: traditional french food, cocktail party and catering.

Industry/Entity Type

Catering

```html
<!DOCTYPE html>
<html lang="en">
<head>
<meta charset="utf-8">
<title>Maison Corvel – Business Cards</title>
<link rel="stylesheet" href="https://fonts.googleapis.com/css2?family=Ubuntu:wght@400;500&display=swap">
<style>
  :root {
    --paper: #ffffff;
    --navy: #2e3192;
    --red: #be1e2d;
    --ink: #1a1a1a;
    --edge: #3b3b3b;
    --font: "Ubuntu", sans-serif;
  }
  * { margin: 0; padding: 0; box-sizing: border-box; }
  html, body { width: 848px; height: 1200px; overflow: hidden; background: var(--paper); }
  body { position: relative; font-family: var(--font); }

  .card { position: absolute; overflow: hidden; border-radius: 18px; border: 1px solid var(--edge); }

  /* Front card (landscape) */
  .card-front { left: 156px; top: 136px; width: 557px; height: 308px; background: var(--navy); }
  .front-top { position: absolute; left: 0; top: 0; width: 100%; height: 126px; background: var(--paper); }
  .front-band { position: absolute; left: 0; top: 126px; width: 100%; height: 45px; background: var(--red); }
  .holder { position: absolute; left: 29px; top: 139px; font-size: 18px; color: var(--paper); }
  .holder .role { color: var(--navy); }
  .brand { position: absolute; display: flex; flex-direction: column; align-items: center; gap: 8px; color: var(--ink); font-weight: 500; }
  .brand .mark { width: 34px; height: 34px; border-radius: 50%; background: var(--red); }
  .brand .name { font-size: 17px; letter-spacing: 0.5px; text-transform: uppercase; }
  .card-front .brand { left: 318px; top: 26px; width: 200px; }
  .contact { position: absolute; right: 307px; top: 200px; text-align: right; color: var(--paper); font-size: 19px; line-height: 23px; }
  .services { list-style: none; position: absolute; color: var(--paper); font-size: 19px; line-height: 24px; }
  .card-front .services { left: 301px; top: 200px; }

  /* Back card (portrait) */
  .card-back { left: 295px; top: 530px; width: 301px; height: 541px; background: var(--navy); }
  .card-back svg { position: absolute; left: 0; top: 0; }
  .card-back .brand { left: 0; width: 100%; top: 178px; }
  .card-back .services { left: 0; width: 100%; top: 289px; text-align: center; color: var(--red); font-size: 18px; line-height: 22px; }
</style>
</head>
<body>
  <section class="card card-front">
    <div class="front-top"></div>
    <div class="front-band"></div>
    <div class="brand">
      <span class="mark"></span>
      <span class="name">Maison Corvel</span>
    </div>
    <p class="holder">Étienne Valmont <span class="role">Owner</span></p>
    <div class="contact">
      <p>etienne@corvel.fr</p>
      <p>0431275864</p>
    </div>
    <ul class="services">
      <li>Traditional french food</li>
      <li>Cocktail party</li>
      <li>Catering</li>
    </ul>
  </section>

  <section class="card card-back">
    <svg width="301" height="541" viewBox="0 0 301 541" aria-hidden="true">
      <ellipse cx="150.5" cy="248" rx="270" ry="136" fill="var(--red)"/>
      <ellipse cx="150.5" cy="253" rx="262" ry="118" fill="var(--paper)"/>
    </svg>
    <div class="brand">
      <span class="mark"></span>
      <span class="name">Maison Corvel</span>
    </div>
    <ul class="services">
      <li>Traditional french food</li>
      <li>Cocktail party</li>
      <li>Catering</li>
    </ul>
  </section>
</body>
</html>
```